Plakat-Design für Herbstausstellung
Zielgruppe
Wir sind im Motorradhandel, inkl. Motorrad Bekleidung/Zubehör, tätig. Für unsere Herbstausstellung brauchen wir ein neues Plakat-Design. Unsere Zielgruppe sind im allgemeinen Männer und Frauen im Alter von 18-65 Jahre.
Aufgabenstellung
Das Plakat sollte Hochformat sein.
Angaben welche ersichtlich sein sollten: Unser Logo (Velo Kranz);Herbst-Ausstellung; Datum der Herbstausstellung (20.-22.10.17); Öffnungszeiten (Fr. 14-19h/Sa. 8-19h/So. 9-16h); Saisonausverkauf mit -20% auf Motorradbekleidung und Zubehör (nur auf nicht reduzierte Lagerware); Unsere Livemusik im Festzelt ( Freitag ab 20.00 Uhr Vinyl Abend mit Dustrider, Samstag ab 20.00 Uhr Festmusik mit Bergklang-Ost, Sonntag Matinée 09.00-16.00 Uhr), www.velo-kranz.ch)<- kann klein dargestellt werden; Unsere Markenvertretungen (QRZ, FVL, Harimo)
Vom Design her ist der Kreativität keine Grenze gesetzt (In den Dateianhängen ist unser altes Plakat-Design beigefügt, als Anhaltspunkt für den Inhalt). Es sollte modern und einladend wirken. Wir verwenden im Normalfall den Font "Impact", dies stellt aber kein Killerkriterium dar.

```html
<!DOCTYPE html>
<html lang="de">
<head>
<meta charset="utf-8">
<title>Herbstausstellung – Velo Kranz</title>
<link href="https://fonts.googleapis.com/css2?family=Anton&family=Montserrat:wght@500;700&family=Parisienne&display=swap" rel="stylesheet">
<style>
  :root{
    --paper:#f3d9c6;
    --red:#e3000f;
    --brown:#8c1c10;
    --ribbon:#a83019;
    --ribbon-dark:#7a2010;
    --white:#ffffff;
    --band-edge:#9a9a9a;
    --ink:#2a1a14;
    --leaf-a:#e0531c;
    --leaf-b:#f2a33a;
  }
  *{margin:0;padding:0;box-sizing:border-box}
  html,body{width:849px;height:1200px;overflow:hidden;background:var(--paper)}
  .poster{position:relative;width:849px;height:1200px;background:var(--paper);overflow:hidden;font-family:"Montserrat",sans-serif;color:var(--brown)}
  .abs{position:absolute}
  .leaves-top{left:0;top:0;width:470px;height:360px;
    background:radial-gradient(ellipse at 18% 12%,var(--leaf-a) 0%,rgba(236,120,40,.75) 32%,rgba(242,163,58,.35) 55%,rgba(243,217,198,0) 75%)}
  .leaves-bottom{right:0;bottom:0;width:330px;height:200px;
    background:radial-gradient(ellipse at 80% 85%,rgba(224,83,28,.8) 0%,rgba(242,163,58,.45) 45%,rgba(243,217,198,0) 75%)}
  .logo{left:548px;top:43px;width:260px;height:87px;background:var(--white);display:flex;align-items:center;justify-content:center}
  .logo-name{font-family:"Anton",sans-serif;font-size:36px;color:var(--red);letter-spacing:1px;text-transform:uppercase}
  .script{font-family:"Parisienne",cursive;color:var(--brown)}
  .title-script{left:0;width:849px;top:118px;text-align:center;font-size:128px;line-height:1;padding-left:120px}
  .title-main{left:0;width:849px;top:232px;text-align:center;font-family:"Anton",sans-serif;font-size:116px;line-height:1.1;color:var(--red);letter-spacing:3px}
  .ribbon{left:205px;top:358px;width:440px;height:122px}
  .ribbon-text{left:0;width:849px;top:386px;text-align:center;font-family:"Anton",sans-serif;font-size:30px;line-height:40px;color:var(--white);letter-spacing:.5px;transform:rotate(1.5deg)}
  .rule{top:412px;width:160px;height:22px}
  .rule-left{left:40px}
  .rule-right{left:650px}
  .hours{left:0;width:849px;top:494px;text-align:center;font-family:"Anton",sans-serif;font-size:29px;line-height:40px;color:var(--brown);letter-spacing:.3px}
  .sale-head{left:0;width:849px;top:585px;text-align:center;font-family:"Anton",sans-serif;font-size:62px;line-height:1.2;color:var(--red);letter-spacing:2px}
  .sale-line{left:0;width:849px;top:666px;text-align:center;font-weight:700;font-size:27px;letter-spacing:.6px}
  .sale-note{left:0;width:849px;top:707px;text-align:center;font-weight:500;font-size:13.5px}
  .brands{left:0;top:736px;width:849px;height:101px;background:var(--white);border-top:4px solid var(--band-edge);border-bottom:4px solid var(--band-edge)}
  .brands-label{position:absolute;left:118px;top:13px;width:120px;text-align:center;font-family:"Anton",sans-serif;font-size:17px;line-height:22px;color:var(--red)}
  .brand{position:absolute;top:0;height:93px;display:flex;align-items:center;gap:10px;font-family:"Anton",sans-serif;font-size:28px;color:var(--ink);letter-spacing:1px}
  .brand-mark{display:block;flex:none}
  .brand-qrz{left:286px}
  .brand-fvl{left:441px}
  .brand-harimo{left:580px}
  .live-head{left:238px;top:866px;font-family:"Anton",sans-serif;font-size:62px;line-height:1.1;color:var(--red);letter-spacing:1px}
  .live-sub{left:402px;top:918px;font-size:42px;line-height:1;transform:rotate(-8deg);transform-origin:left bottom;white-space:nowrap}
  .day{top:976px;width:280px}
  .day-fr{left:40px}
  .day-sa{left:342px}
  .day-so{left:643px}
  .day-code{position:absolute;left:0;top:0;font-family:"Anton",sans-serif;font-size:76px;line-height:1;color:var(--red)}
  .day-time{position:absolute;top:10px;font-family:"Anton",sans-serif;font-size:24px;line-height:1.2;color:var(--brown);text-align:center}
  .day-time sup{font-size:13px;vertical-align:9px}
  .day-fr .day-time,.day-sa .day-time{left:104px}
  .day-so .day-time{left:90px}
  .sep{top:975px;width:0;height:150px;border-left:2px dotted var(--brown)}
  .sep-1{left:272px}
  .sep-2{left:565px}
  .act{top:1057px;text-align:center;font-weight:700;font-size:20.5px;line-height:24px;letter-spacing:.5px}
  .act-fr{left:30px;width:185px}
  .act-sa{left:320px;width:210px;top:1070px}
  .act-so{left:640px;width:170px;top:1082px}
  .footer{left:40px;top:1157px;font-weight:700;font-size:13.5px;line-height:17px;color:var(--brown);letter-spacing:.3px;font-style:normal}
</style>
</head>
<body>
<div class="poster">
  <div class="abs leaves-top" role="img" aria-label="Herbstlaub in Orange, Rot und Gelb"></div>
  <div class="abs leaves-bottom" role="img" aria-label="Herbstlaub in Orange und Gelb"></div>

  <div class="abs logo"><span class="logo-name">Velo Kranz</span></div>

  <div class="abs script title-script">Herbst</div>
  <h1 class="abs title-main">AUSSTELLUNG</h1>

  <svg class="abs ribbon" viewBox="0 0 440 122" aria-hidden="true">
    <polygon points="0,52 60,52 60,110 30,110 50,83 0,122" fill="var(--ribbon)"/>
    <polygon points="440,52 380,52 380,110 410,110 390,83 440,122" fill="var(--ribbon)"/>
    <polygon points="60,100 90,110 60,110" fill="var(--ribbon-dark)"/>
    <polygon points="380,100 350,110 380,110" fill="var(--ribbon-dark)"/>
    <path d="M45,8 Q220,0 395,14 L395,100 Q220,86 45,96 Z" fill="var(--ribbon)"/>
  </svg>
  <div class="abs ribbon-text">20. – 22. OKTOBER 2017</div>
  <svg class="abs rule rule-left" viewBox="0 0 160 22" aria-hidden="true">
    <path d="M0,2 Q80,14 160,16" stroke="var(--brown)" fill="none" stroke-width="1.5"/>
    <path d="M0,8 Q80,20 160,21" stroke="var(--brown)" fill="none" stroke-width="1.5"/>
  </svg>
  <svg class="abs rule rule-right" viewBox="0 0 160 22" aria-hidden="true">
    <path d="M0,16 Q80,14 160,2" stroke="var(--brown)" fill="none" stroke-width="1.5"/>
    <path d="M0,21 Q80,20 160,8" stroke="var(--brown)" fill="none" stroke-width="1.5"/>
  </svg>

  <p class="abs hours">FR. 14-19 Uhr | SA. 8-19 Uhr | SO. 9-16 Uhr</p>

  <h2 class="abs sale-head">SAISONABVERKAUF</h2>
  <p class="abs sale-line">-20% auf Motorradbekleidung und Zubehör</p>
  <p class="abs sale-note">Nur auf nicht reduzierte Lagerware</p>

  <section class="abs brands">
    <div class="brands-label">Unsere<br>Marken-<br>vertretung</div>
    <div class="brand brand-qrz"><svg class="brand-mark" width="26" height="26" aria-hidden="true"><circle cx="13" cy="13" r="12" fill="var(--ink)"/></svg>QRZ</div>
    <div class="brand brand-fvl"><svg class="brand-mark" width="26" height="26" aria-hidden="true"><rect width="26" height="26" fill="var(--leaf-a)"/></svg>FVL</div>
    <div class="brand brand-harimo"><svg class="brand-mark" width="26" height="26" aria-hidden="true"><rect width="26" height="26" fill="var(--ink)"/></svg>Harimo</div>
  </section>

  <h2 class="abs live-head">LIVE-MUSIK</h2>
  <div class="abs script live-sub">im großen Festzelt</div>

  <div class="abs day day-fr"><span class="day-code">FR</span><span class="day-time">AB<br>20<sup>00</sup></span></div>
  <div class="abs day day-sa"><span class="day-code">SA</span><span class="day-time">AB<br>20<sup>00</sup></span></div>
  <div class="abs day day-so"><span class="day-code">SO</span><span class="day-time">AB<br>9<sup>00</sup>-16<sup>00</sup></span></div>

  <div class="abs sep sep-1"></div>
  <div class="abs sep sep-2"></div>

  <p class="abs act act-fr">Vinyl Abend<br>mit<br>Dustrider</p>
  <p class="abs act act-sa">Festmusik mit<br>Bergklang-Ost</p>
  <p class="abs act act-so">Matinée</p>

  <address class="abs footer">Feldmattweg 14, 5034 Suhrental,<br>Tel. 062 555 41 20, www.velo-kranz.ch</address>
</div>
</body>
</html>
```